ROOFING SALES QUOTE TEMPLATE / BROCHURE

I am a roofing contractor looking to elevate and simplify the sales presentation of our roof installation services to our customers through a slick/company branded bid form or brochure. Im looking more for design elements in a template format that can be used/modified to have information populated based on unique customer needs.
I would like to have the bid form or brochure present 3 options to homeowners: GOOD / BETTER / BEST

Potentially include pages with details to educate the homeowners on the components of a roof, the material /product specifications included in each of the GOOD/BETTER/BEST options, our insurance information, licensing, etc.

For example: Homeowner Dalton is looking to have his asphalt shingle roof replaced on his residential home. Dalton knows nothing about roofing, but knows the roof is getting old.
Keelstone Roofing would like to present him with three replacement options, with different price points:
OPTION 1 (Good) = Remove and replace existing roof with new shingle tier 1 quality
OPTION 2 (BETTER) = remove and replace existing roof with new shingle tier 2 quality and better warranty
OPTION 3 (BEST) = remove and replace existing roof with new highest quality shingle and highest grade warranty

I would like one page to concisely present all three options, visually simple with price, and option summaries

One page which essentially educates on the components of a roof (attic space, trusses/rafters/eaves , plywood decking, roofing felts/underlayment, shingle material, metal flashings, ridge and hip shingles, ventilation, etc) -graphic?

One or more pages that show more specific details/scope of each of the options presented (unless this is TMI and we can provide a URL

Another page showcasing our license, insurance, bonds, certification, etc.

For branding, we are partnered with the manufacturer HMT in case we can co-brand anything.

Most of these will be used electronically and filled out as a PDF or similar.

Target Market(s)

Residential and commercial building owners looking for roof replacements

Industry/Entity Type

Roofing (USA - California)

Requirements
Must have
• present 3 options to homeowners: GOOD / BETTER / BEST -design must match logo colors
Nice to have
• One or more pages that show more specific details/scope of each of the options presented (unless this is TMI and we can provide a URL
Should not have
• too much wordiness

```html
<!DOCTYPE html>
<html lang="en">
<head>
<meta charset="utf-8">
<title>Keelstone Roofing – Proposal Template Pages</title>
<link href="https://fonts.googleapis.com/css2?family=Roboto+Condensed:wght@400;700&family=Roboto:wght@400;500;700&display=swap" rel="stylesheet">
<style>
:root{
  --orange:#e8702a;
  --orange-soft:#f3a26f;
  --ink:#222222;
  --text:#4a4a4a;
  --muted:#8a8a8a;
  --rule:#d6d6d6;
  --paper:#ffffff;
  --stage:#8e9194;
  --dark:#2d2d2d;
  --light:#dcdcdc;
}
*{margin:0;padding:0;box-sizing:border-box}
html,body{width:1200px;height:655px;overflow:hidden;background:var(--stage)}
body{position:relative;font-family:"Roboto",Arial,sans-serif;color:var(--text)}
.page{position:absolute;background:var(--paper);overflow:hidden}
.p1{left:15px;top:19px;width:358px;height:303px}
.p2{left:412px;top:19px;width:364px;height:303px}
.p3{left:816px;top:19px;width:366px;height:303px}
.p4{left:15px;top:348px;width:358px;height:293px}
.p5{left:412px;top:348px;width:364px;height:293px}
.p6{left:816px;top:348px;width:366px;height:293px}
.abs{position:absolute}
.bar{position:absolute;background:var(--orange)}
.top-bar{top:0;right:0;width:118px;height:9px}
.side-bar{left:0;top:0;width:12px;height:110px}
h1,h2,h3{font-family:"Roboto Condensed",Arial,sans-serif;color:var(--ink);font-weight:700;position:absolute;line-height:1}
h1{font-size:22px;letter-spacing:-.3px}
h2{font-size:15px}
.brand{position:absolute;right:14px;display:flex;align-items:center;gap:4px;font-family:"Roboto Condensed",Arial,sans-serif;font-weight:700;font-size:10px;color:var(--orange);line-height:1.1}
.brand i{display:block;width:9px;height:9px;background:var(--dark);flex:none}
.photo{position:absolute}
.small{font-size:6px;line-height:1.45;color:var(--text)}
.bullets{list-style:none}
.bullets li{font-size:6px;line-height:1.4;margin-bottom:4px;padding-left:8px;position:relative}
.bullets li::before{content:"";position:absolute;left:0;top:2px;width:3px;height:3px;background:var(--orange);border-radius:50%}
.bullets b{display:block;font-size:7px;color:var(--ink)}
.label{position:absolute;font-size:7px;color:var(--ink);white-space:nowrap}
.p1 .meta{position:absolute;left:34px;top:238px;font-size:11px;color:var(--ink);line-height:1.3}
.tiers{position:absolute;top:74px;left:38px;width:300px;display:flex;justify-content:space-between;font-family:"Roboto Condensed",Arial,sans-serif;font-weight:700;font-size:22px;color:var(--orange)}
.tiers span.sep{color:var(--muted);font-weight:400}
.tier-note{position:absolute;top:116px;font-size:7px;color:var(--ink);line-height:1.3;display:flex;gap:4px}
.tier-note i{display:block;width:9px;height:9px;border-radius:50%;background:var(--orange);flex:none}
.card{position:absolute;width:104px;height:40px;border-radius:3px;display:flex;align-items:center;justify-content:center;gap:6px;font-size:7px;color:#fff;line-height:1.2}
.card.dark{background:var(--dark)}
.card.orange{background:var(--orange)}
.card .ico{width:12px;height:12px;border:1.2px solid currentColor;border-radius:50%}
.price{position:absolute;width:104px;height:46px;border-radius:3px;text-align:center;color:#fff;font-family:"Roboto Condensed",Arial,sans-serif}
.price b{display:block;font-size:23px;margin-top:4px;line-height:1}
.price span{font-size:9px}
.price.dark{background:var(--dark)}
.price.grey{background:var(--light);color:var(--ink)}
.price.orange{background:var(--orange)}
.btn{position:absolute;background:var(--orange);color:#fff;font-family:"Roboto Condensed",Arial,sans-serif;font-size:8px;font-weight:700;text-align:center;letter-spacing:.5px;line-height:15px}
.icon-row{position:absolute;display:flex}
.icon-item{width:48px;text-align:center;font-size:7px;color:var(--ink);line-height:1.2}
.icon-item svg{display:block;margin:0 auto 4px}
.badge-round{position:absolute;border-radius:50%;background:var(--dark)}
.badge-rect{position:absolute;background:var(--dark);border-radius:2px}
.notes{position:absolute;display:flex;align-items:center;gap:5px;font-size:7px;color:var(--ink);font-weight:500}
.notes i{width:10px;height:10px;border-radius:50%;border:1.5px solid var(--orange);display:block}
.edu{position:absolute;top:200px;left:22px;display:flex;gap:10px}
.edu .col{width:62px;text-align:center}
.edu b{display:block;font-size:7px;color:var(--ink);margin:4px 0 2px}
.edu p{font-size:5.5px;line-height:1.4}
</style>
</head>
<body>

<section class="page p1">
  <div class="bar top-bar"></div>
  <h1 style="left:34px;top:34px">Roof Replacement Proposal</h1>
  <div class="bar" style="left:0;top:98px;width:40px;height:100px"></div>
  <div class="bar" style="right:0;top:98px;width:40px;height:100px"></div>
  <div class="photo" role="img" aria-label="Photo of a grey-sided two-storey house with a new dark shingle roof" style="left:34px;top:66px;width:291px;height:156px;background:linear-gradient(180deg,#e6e8ea 0%,#5b5e63 38%,#8b939b 62%,#a9b1b8 100%)"></div>
  <div class="meta">Protecting Homes Since 1980<br>Client Name<br>4DD403B</div>
  <div class="brand" style="right:34px;top:244px;font-size:13px"><i style="width:12px;height:12px"></i><span>KEELSTONE<br>ROOFING</span></div>
  <div class="bar" style="left:0;bottom:0;width:146px;height:10px"></div>
</section>

<section class="page p2">
  <div class="bar top-bar"></div>
  <div class="bar side-bar"></div>
  <h1 style="left:42px;top:36px">Three Option Proposal</h1>
  <div class="brand" style="top:30px"><i></i><span>KEELSTONE<br>ROOFING</span></div>
  <div class="tiers"><span>GOOD</span><span class="sep">|</span><span>BETTER</span><span class="sep">|</span><span>BEST</span></div>
  <div class="tier-note" style="left:30px"><i></i>Tier 1 Shingles<br>with Warranty</div>
  <div class="tier-note" style="left:140px"><i></i>Tier 2 Shingles<br>with Warranty</div>
  <div class="tier-note" style="left:240px"><i></i>Highest quality shingles<br>+ Top Warranty</div>
  <div class="card dark" style="left:18px;top:160px"><span class="ico"></span>Base Option<br>Tier</div>
  <div class="card orange" style="left:130px;top:160px"><span class="ico"></span>Base Option<br>Tier</div>
  <div class="card orange" style="left:242px;top:160px"><span class="ico"></span>Base Option<br>Tier</div>
  <div class="price dark" style="left:18px;top:212px"><b>$Price</b><span>What's Included</span></div>
  <div class="price grey" style="left:130px;top:212px"><b>$Price</b><span>What's Included</span></div>
  <div class="price orange" style="left:242px;top:212px"><b>$Price</b><span>What's Included</span></div>
  <div class="abs" style="left:18px;top:270px;width:328px;height:1px;background:var(--rule)"></div>
  <p class="small abs" style="left:18px;top:276px;width:328px">Each option includes full tear-off, new underlayment, cleanup and a final inspection by our crew before the job is signed off.</p>
</section>

<section class="page p3">
  <div class="bar top-bar"></div>
  <div class="bar" style="left:0;top:0;width:12px;height:100px"></div>
  <div class="photo" role="img" aria-label="Photo of a grey house with a dark shingle roof" style="left:14px;top:14px;width:190px;height:54px;background:linear-gradient(180deg,#f2f3f4 0%,#9aa3ab 55%,#7c858d 100%)"></div>
  <div class="abs" style="left:14px;top:66px;width:352px;height:8px;background:#4b4d50"></div>
  <h2 style="left:36px;top:96px">Targeted Audiences</h2>
  <ul class="bullets abs" style="left:36px;top:116px;width:130px">
    <li>Homeowners replacing an aging asphalt roof</li>
    <li><b>Warranty</b>Manufacturer and workmanship coverage included</li>
    <li><b>Reliability</b>Proven crews and clean job sites</li>
    <li><b>Durability</b>Materials rated for California weather</li>
  </ul>
  <div class="notes" style="left:36px;top:255px"><i></i>Contractor Notes</div>
  <p class="small abs" style="left:36px;top:270px;width:130px">Notes from your estimator about site access and timing</p>
  <h2 style="left:180px;top:96px">Detailed Scope</h2>
  <ul class="bullets abs" style="left:180px;top:116px;width:160px">
    <li>Scope items listed for each option</li>
    <li><b>Flashing</b>New metal flashing at walls and valleys</li>
    <li>Roof ventilation reviewed and upgraded</li>
  </ul>
  <div class="btn" style="left:180px;top:194px;width:158px;height:15px">DETAILED SCOPE</div>
  <div class="icon-row" style="left:180px;top:224px;gap:6px">
    <div class="icon-item"><svg width="26" height="26" viewBox="0 0 26 26" fill="none" stroke="#333" stroke-width="1.5"><rect x="4" y="8" width="18" height="14"/><path d="M2 9 13 2l11 7"/><path d="M10 22v-6h6v6"/></svg>Warranty</div>
    <div class="icon-item"><svg width="26" height="26" viewBox="0 0 26 26"><path d="M2 14 13 8l11 6-11 6z" fill="#e8702a"/><path d="M2 10 13 4l11 6-11 6z" fill="#f3a26f"/></svg>Weather Barrier</div>
    <div class="icon-item"><svg width="26" height="26" viewBox="0 0 26 26" fill="none" stroke="#333" stroke-width="1.5"><path d="M13 2 24 13 13 24 2 13z"/><path d="M9 13l3 3 5-6"/></svg>Warranty</div>
  </div>
</section>

<section class="page p4">
  <div class="bar top-bar"></div>
  <h1 style="left:36px;top:28px;font-size:20px">Roof System Components</h1>
  <div class="brand" style="top:26px"><i></i><span>KEELSTONE<br>ROOFING</span></div>
  <h2 style="left:36px;top:62px">Detailed Scope</h2>
  <ul class="bullets abs" style="left:36px;top:84px;width:150px">
    <li><b>Shingles</b>Remove existing shingles down to decking</li>
    <li>Replace damaged decking where needed</li>
    <li>Install synthetic underlayment across roof</li>
    <li>New drip edge and step flashing</li>
    <li>Ridge caps and hip shingles installed</li>
    <li>Vents checked and balanced for airflow</li>
  </ul>
  <div class="notes" style="left:36px;top:232px"><i></i>Contractor Notes</div>
  <p class="small abs" style="left:36px;top:247px;width:150px">Write project-specific notes and scope changes here.</p>
  <span class="label" style="left:206px;top:88px">Attic</span>
  <span class="label" style="left:300px;top:88px">Decking</span>
  <div class="photo" role="img" aria-label="Cutaway illustration of roof framing showing attic, decking and shingle layers" style="left:218px;top:100px;width:104px;height:100px;background:linear-gradient(150deg,#f0dfc4 0%,#d9b98c 55%,#9a9a9a 100%)"></div>
  <span class="label" style="left:200px;top:206px">Decking</span>
  <span class="label" style="left:306px;top:206px">Shingles</span>
  <span class="label" style="left:224px;top:222px">Felts</span>
  <span class="label" style="left:296px;top:222px">Vents</span>
  <div class="badge-round" style="left:226px;top:248px;width:34px;height:34px"></div>
  <div class="badge-rect" style="left:270px;top:256px;width:64px;height:18px"></div>
</section>

<section class="page p5">
  <div class="bar top-bar"></div>
  <div class="bar side-bar" style="height:90px"></div>
  <h1 style="left:40px;top:30px;font-size:19px">Educational Roof Components</h1>
  <div class="brand" style="top:26px"><i></i><span>KEELSTONE<br>ROOFING</span></div>
  <div class="photo" role="img" aria-label="Technical drawing of a roof truss with decking, underlayment, shingles and ridge cap" style="left:90px;top:68px;width:190px;height:104px;background:linear-gradient(180deg,#5a5a5a 0%,#d8b585 40%,#e6cba3 100%)"></div>
  <span class="label" style="left:44px;top:98px">Rafters</span>
  <span class="label" style="left:44px;top:112px">Trusses</span>
  <span class="label" style="left:34px;top:126px">Underlayment</span>
  <span class="label" style="left:288px;top:96px">Decking</span>
  <span class="label" style="left:288px;top:110px">Shingles</span>
  <span class="label" style="left:288px;top:124px">Ventilation</span>
  <span class="label" style="left:288px;top:138px">Ridge Caps</span>
  <span class="label" style="left:124px;top:180px">Flashing</span>
  <span class="label" style="left:190px;top:180px">Rafters</span>
  <span class="label" style="left:250px;top:180px">Vents</span>
  <div class="edu">
    <div class="col"><svg width="24" height="22" viewBox="0 0 24 22" fill="none" stroke="#333" stroke-width="1.4"><path d="M2 10 12 2l10 8"/><rect x="5" y="9" width="14" height="12"/></svg><b>Roofs</b><p>The full system that keeps your home dry.</p></div>
    <div class="col"><svg width="24" height="22" viewBox="0 0 24 22"><path d="M12 1 21 4v7c0 5-4 9-9 10C7 20 3 16 3 11V4z" fill="#e8702a"/></svg><b>Warranties</b><p>Coverage terms for each option tier.</p></div>
    <div class="col"><svg width="24" height="22" viewBox="0 0 24 22" fill="none" stroke="#333" stroke-width="1.4"><rect x="5" y="2" width="14" height="19"/><path d="M8 8h8M8 12h8M8 16h5"/></svg><b>Records</b><p>Permits, photos and inspection reports.</p></div>
    <div class="col"><svg width="24" height="22" viewBox="0 0 24 22"><path d="M2 13 12 8l10 5-10 5z" fill="#e8702a"/><path d="M2 9 12 4l10 5-10 5z" fill="#9a9a9a"/></svg><b>Quality</b><p>Layered materials built to last.</p></div>
  </div>
  <div class="badge-round" style="left:310px;top:214px;width:40px;height:40px;background:var(--orange)"></div>
</section>

<section class="page p6">
  <div class="bar top-bar"></div>
  <div class="bar side-bar" style="height:70px"></div>
  <h1 style="left:26px;top:28px">Credentials &amp; Trust</h1>
  <div class="brand" style="top:26px"><i></i><span>KEELSTONE<br>ROOFING</span></div>
  <h2 style="left:26px;top:64px;font-weight:400;font-size:13px;line-height:1.25">Licence<br>Roofing Contractor</h2>
  <p class="small abs" style="left:26px;top:100px;width:150px">California licensed roofing contractor, fully insured and bonded for residential and commercial work.</p>
  <h2 style="left:26px;top:142px">Certification</h2>
  <p class="small abs" style="left:26px;top:160px;width:150px">Factory certified installer with trained crews and ongoing product education.</p>
  <p class="small abs" style="left:26px;top:190px;width:150px"><b style="color:var(--ink)">Bonds &amp; Insurance</b><br>Policy and bond numbers listed here.</p>
  <div class="badge-rect" style="left:26px;top:236px;width:28px;height:28px"></div>
  <div class="badge-round" style="left:64px;top:236px;width:28px;height:28px"></div>
  <div class="badge-round" style="left:102px;top:236px;width:28px;height:28px"></div>
  <div class="photo" role="img" aria-label="Photo of a finished home with a new roof and trees behind" style="left:190px;top:62px;width:146px;height:92px;background:linear-gradient(180deg,#dfe3e6 0%,#a7afb5 50%,#7d8a74 100%)"></div>
  <p class="small abs" style="left:190px;top:166px;width:150px">Trusted by local homeowners for decades. Every project is backed by written warranties.</p>
  <p class="small abs" style="left:190px;top:200px;width:150px">We handle permits, inspections and cleanup so your project stays simple and on schedule.</p>
  <p class="small abs" style="left:190px;top:238px;width:150px">Ask for references and recent project photos from your neighbourhood.</p>
</section>

</body>
</html>
```